Web Design Project

We need a web design new company based in Australia. We're a search engine marketing company who predominantly manages Vexlo bidlines campaigns.
Currently still deciding on a business name so lets use “Marlow Taps” for now.
Target market....
small to medium size businesses
- more clicks to their website from the 1st page of Vexlo
- more relevant, (higher quality) clicks
- higher return on investment from their bidlines campaign
- more sales, leads, (conversions)
We'd like clean, simple, semi-professional as we'd like to pick up some high end corporate clients.
A website that we love the look and feel of – but they’re a direct competitor so can’t be too similar in design.
http://www.brendvale.com.au/search-engine-marketing.html
**please check portfolio on this web page..they designs are absolutely stunning!! http://www.brendvale.com.au/website-design.html
Updates
Please refer to the attached file, a rough sketch of my web page.
place replace...."Afraid your bidlines campaign is underperforming with,....
Industry/Entity Type
Business
Look and feel

```html
<!DOCTYPE html>
<html lang="en">
<head>
<meta charset="utf-8">
<title>Marlow Taps</title>
<link href="https://fonts.googleapis.com/css2?family=Bebas+Neue&family=Quicksand:wght@500;700&display=swap" rel="stylesheet">
<style>
  :root {
    --sky: #2ba1d2;
    --sky-light: #6ccbdf;
    --lime: #c6e92b;
    --ink: #1f1f1f;
    --bar-top: #4a4a4a;
    --bar-bottom: #141414;
    --heading-blue: #2a9bcf;
    --white: #ffffff;
    --body-text: #111111;
  }
  * { box-sizing: border-box; margin: 0; padding: 0; }
  html, body { width: 1200px; height: 1150px; overflow: hidden; }
  body {
    position: relative;
    background: radial-gradient(ellipse 520px 420px at 520px 120px, var(--sky-light), var(--sky) 80%);
    background-color: var(--sky);
    font-family: "Quicksand", sans-serif;
  }
  .brand {
    position: absolute; left: 160px; top: 40px;
    font-family: "Quicksand", sans-serif; font-weight: 700;
    font-size: 40px; line-height: 1; color: var(--lime);
  }
  .phone-tab {
    position: absolute; left: 812px; top: 0; width: 221px; height: 49px;
    background: linear-gradient(var(--bar-top), var(--bar-bottom));
    border-radius: 0 0 8px 8px;
    color: var(--white); font-family: "Bebas Neue", sans-serif;
    font-size: 27px; letter-spacing: 1px;
    display: flex; align-items: center; justify-content: center;
  }
  .main-nav {
    position: absolute; left: 124px; top: 137px; width: 951px; height: 48px;
    background: linear-gradient(var(--bar-top), var(--bar-bottom) 55%);
    border-radius: 8px; box-shadow: 0 3px 8px rgba(0,0,0,.35);
    display: flex; align-items: center; padding-left: 41px;
  }
  .main-nav a {
    color: var(--white); text-decoration: none; font-weight: 700;
    font-size: 16px; letter-spacing: 1.5px; text-transform: uppercase;
    margin-right: 44px;
  }
  .main-nav a.current { color: var(--lime); }
  .hero-title {
    position: absolute; left: 156px; top: 282px; width: 520px;
    font-family: "Bebas Neue", sans-serif; color: var(--white);
    font-weight: 400; line-height: .98; text-shadow: 0 2px 4px rgba(0,0,0,.15);
  }
  .hero-title span { display: block; white-space: nowrap; }
  .hero-title .l1 { font-size: 71px; }
  .hero-title .l2 { font-size: 57px; }
  .hero-title .l3 { font-size: 34px; }
  .health-check {
    position: absolute; left: 699px; top: 275px; width: 343px; height: 202px;
    background: linear-gradient(#3b3b3b, #111 60%);
    border-radius: 7px; color: var(--white); padding: 20px 27px;
  }
  .health-check h2 { font-weight: 500; font-size: 22px; margin-bottom: 27px; }
  .health-check label { display: block; font-size: 20px; margin-bottom: 6px; }
  .health-check .field {
    width: 290px; height: 37px; background: var(--white); border-radius: 8px;
    box-shadow: inset 0 2px 4px rgba(0,0,0,.35);
  }
  .health-check .step { position: absolute; left: 29px; bottom: 27px; font-size: 20px; }
  .health-check .next {
    position: absolute; right: 26px; bottom: 25px; width: 56px; height: 29px;
    background: linear-gradient(#fafafa, #bbb); border-radius: 8px;
    color: var(--ink); font-family: "Bebas Neue", sans-serif; font-size: 18px;
    display: flex; align-items: center; justify-content: center;
  }
  .services {
    position: absolute; left: 125px; top: 539px; width: 949px; height: 468px;
    background: var(--white); border-radius: 8px;
  }
  .service { position: absolute; top: 40px; width: 290px; height: 400px; }
  .service h3 {
    font-family: "Bebas Neue", sans-serif; font-weight: 400;
    font-size: 38px; color: var(--heading-blue); line-height: 1; white-space: nowrap;
  }
  .service .visual { position: absolute; top: 46px; }
  .service p {
    position: absolute; left: 0; top: 226px; width: 242px;
    font-family: Arial, Helvetica, sans-serif; font-size: 12px;
    line-height: 14.3px; color: var(--body-text);
  }
  .site-footer {
    position: absolute; left: 125px; top: 1029px; width: 949px; height: 44px;
    background: var(--ink); border-radius: 7px;
    display: flex; align-items: center; justify-content: space-between;
    padding: 0 25px; color: var(--white);
    font-family: Arial, Helvetica, sans-serif; font-size: 13px;
  }
  .site-footer a { color: var(--white); text-decoration: none; }
  .site-footer .sep { margin: 0 6px; }
</style>
</head>
<body>
  <div class="brand">Marlow Taps</div>
  <div class="phone-tab">Call 1300 48 5790</div>

  <nav class="main-nav">
    <a class="current" href="#">Home</a>
    <a href="#">About</a>
    <a href="#">Vexlo bidlines</a>
    <a href="#" style="margin-right:52px">Other Services</a>
    <a href="#" style="margin-right:48px">Why Choose Us?</a>
    <a href="#" style="margin-right:0">Contact</a>
  </nav>

  <h1 class="hero-title">
    <span class="l1">Want more sales and</span>
    <span class="l2">leads from your bidlines</span>
    <span class="l3">campaign without increasing your budget?</span>
  </h1>

  <form class="health-check">
    <h2>FREE Bidlines Health Check</h2>
    <label>Step 1: Your Website</label>
    <div class="field"></div>
    <div class="step">Step 1 of 3</div>
    <div class="next">Next</div>
  </form>

  <section class="services">
    <article class="service" style="left:53px">
      <h3>Local Bidlines</h3>
      <div class="visual" role="img" aria-label="Blue illustrated SEO tag hanging from a string"
           style="left:22px;width:186px;height:142px;background:radial-gradient(ellipse at center,#5ab8d8 0%,#1f86b3 55%,#ffffff 75%);"></div>
      <p>Web design or web development is a crucial element to getting businesses online, that's why here at The Tap Works we make it's done right! Websites are the face of most businesses these days and that why it's incredibly important above all that they look good and work properly, it may sound simple, however, it's something which most businesses fail to get right. We believe the 3 most important things to think about when designing a website are:</p>
    </article>
    <article class="service" style="left:341px">
      <h3>National Bidlines</h3>
      <div class="visual" role="img" aria-label="Photo of pink paper arrows around an SEO note on a chalkboard"
           style="left:0;width:246px;height:162px;background:radial-gradient(circle at center,#c9e08a 0%,#e888b8 30%,#1d3838 75%);"></div>
      <p>Web design or web development is a crucial element to getting businesses online, that's why here at The Tap Works we make it's done right! Websites are the face of most businesses these days and that why it's incredibly important above all that they look good and work properly, it may sound simple, however, it's something which most businesses fail to get right. We believe the 3 most important things to think about when designing a website are:</p>
    </article>
    <article class="service" style="left:638px">
      <h3>Ecommerce Bidlines</h3>
      <div class="visual" role="img" aria-label="Photo of a key with a paper tag on a wooden table"
           style="left:1px;width:220px;height:166px;background:linear-gradient(135deg,#b66c2c,#d69248 50%,#a45e24);"></div>
      <p style="left:1px">Web design or web development is a crucial element to getting businesses online, that's why here at The Tap Works we make it's done right! Websites are the face of most businesses these days and that why it's incredibly important above all that they look good and work properly, it may sound simple, however, it's something which most businesses fail to get right. We believe the 3 most important things to think about when designing a website are:</p>
    </article>
  </section>

  <footer class="site-footer">
    <nav>
      <a href="#">Home</a><span class="sep">|</span>
      <a href="#">About</a><span class="sep">|</span>
      <a href="#">Vexlo bidlines</a><span class="sep">|</span>
      <a href="#">Other Services</a><span class="sep">|</span>
      <a href="#">Why Choose us</a><span class="sep">|</span>
      <a href="#">Contact</a>
    </nav>
    <div>Copyright 2012<span class="sep">|</span>All Rights Reserved</div>
  </footer>
</body>
</html>
```